Banner Design Project

We are an Australian online lighting store based in Sydney.
Our website is "www.trelvamart.com.au"
We need someone you can create a 2 banners for our homepage.
We will have 3 banners rotating, the first banner will be our actual banner, the second one will be advertising Free Shipping Insurance and the third will advertising the 30 Day money back guaranty.
Don't be afraid to use words like Risk Free, 30 Day Money back Guaranty! etc....
The banner size:
599 x 186 px
The format should be given in .psd and .jpg
We need something slick and attractive that looks very promotional.
The banner should have the same look and feel as the website.
We are looking for someone long term, so if the job goes well, we might ask the person to design regularly for us in the future.

```html
<!DOCTYPE html>
<html lang="en">
<head>
<meta charset="utf-8">
<title>Trelvamart – Free Shipping Insurance</title>
<link rel="stylesheet" href="https://fonts.googleapis.com/css2?family=Archivo+Black&family=Arimo:wght@400;700&display=swap">
<style>
  :root {
    --bg-top: #f4f4f4;
    --bg-bottom: #dcdcdc;
    --strip: #e9e9e9;
    --strip-line: #c9c9c9;
    --caption: #8c8c8c;
    --letter-edge: #2d5a8c;
    --bar-light: #5a8cc0;
    --bar-mid: #2f639a;
    --bar-dark: #1f4a78;
    --brand: #f07c1c;
  }
  html, body {
    margin: 0;
    padding: 0;
    width: 1200px;
    height: 373px;
    overflow: hidden;
    background: #ffffff;
  }
  .banner {
    position: relative;
    width: 1200px;
    height: 373px;
    background: linear-gradient(180deg, var(--bg-top) 0%, var(--bg-bottom) 100%);
    overflow: hidden;
  }
  .headline {
    position: absolute;
    left: 14px;
    top: 14px;
    width: 790px;
    height: 250px;
  }
  .caption-strip {
    position: absolute;
    left: 0;
    top: 258px;
    width: 1200px;
    height: 56px;
    background: linear-gradient(180deg, var(--strip) 0%, #f2f2f2 100%);
    border-top: 2px solid var(--strip-line);
  }
  .caption {
    position: absolute;
    left: 30px;
    top: 262px;
    margin: 0;
    font-family: "Arimo", Arial, sans-serif;
    font-weight: 400;
    font-size: 47px;
    letter-spacing: 7.4px;
    line-height: 56px;
    color: var(--caption);
    white-space: nowrap;
  }
  .brand {
    position: absolute;
    right: 24px;
    top: 222px;
    display: flex;
    align-items: center;
    gap: 10px;
    font-family: "Arimo", Arial, sans-serif;
    font-weight: 700;
    font-size: 54px;
    letter-spacing: -1px;
    color: var(--brand);
  }
  .brand-dot {
    width: 18px;
    height: 18px;
    border-radius: 50%;
    background: var(--brand);
  }
  .footer-bar {
    position: absolute;
    left: 0;
    bottom: 0;
    width: 1200px;
    height: 58px;
    background: linear-gradient(180deg, var(--bar-mid) 0%, var(--bar-dark) 100%);
    border-top: 6px solid var(--bar-light);
    box-sizing: border-box;
  }
</style>
</head>
<body>
  <div class="banner">
    <svg class="headline" viewBox="0 0 790 250" role="img" aria-label="The word FREE with lamp and light-fitting photographs filling each letter">
      <defs>
        <linearGradient id="fill-f" x1="0" y1="0" x2="0" y2="1">
          <stop offset="0" stop-color="#5b6b4a"/>
          <stop offset="0.5" stop-color="#6e4a33"/>
          <stop offset="1" stop-color="#3a2a22"/>
        </linearGradient>
        <linearGradient id="fill-r" x1="0" y1="0" x2="1" y2="1">
          <stop offset="0" stop-color="#c9a58a"/>
          <stop offset="0.5" stop-color="#7a4a34"/>
          <stop offset="1" stop-color="#b98f78"/>
        </linearGradient>
        <linearGradient id="fill-e1" x1="0" y1="0" x2="1" y2="1">
          <stop offset="0" stop-color="#e7c8ad"/>
          <stop offset="0.5" stop-color="#b07a55"/>
          <stop offset="1" stop-color="#e3c3a8"/>
        </linearGradient>
        <linearGradient id="fill-e2" x1="0" y1="0" x2="1" y2="1">
          <stop offset="0" stop-color="#f3e3c8"/>
          <stop offset="0.45" stop-color="#d84a2a"/>
          <stop offset="1" stop-color="#efe4d4"/>
        </linearGradient>
      </defs>
      <g font-family="Archivo Black, Arial Black, sans-serif" font-size="318" stroke="var(--letter-edge)" stroke-width="5" paint-order="stroke">
        <text x="4" y="238" fill="url(#fill-f)">F</text>
        <text x="190" y="238" fill="url(#fill-r)">R</text>
        <text x="400" y="238" fill="url(#fill-e1)">E</text>
        <text x="594" y="238" fill="url(#fill-e2)">E</text>
      </g>
    </svg>

    <div class="caption-strip"></div>
    <p class="caption">SHIPPING INSURANCE</p>

    <div class="brand"><span class="brand-dot"></span>Trelvamart</div>

    <div class="footer-bar"></div>
  </div>
</body>
</html>
```